Business card Zottelgarten

Business card is for a self-employed dog trainer with own dog school. Name and logo of the dog school are available. Color specifications as well. The design should be classy and minimalist, but also modern. An already existing idea would be: Front: Only the logo Back: Contact data

Font styles to use
Serif
Sans Serif
Other font styles liked:
• Trajan Pro

Colors
f78f20

Requirements
Must have
• Name: Margit Wendler-Rasch Title: Dipl. Dog Trainer Contain my logo Follow my font and color preferences (see files)

```html
<!DOCTYPE html>
<html lang="en">
<head>
<meta charset="utf-8">
<title>Zottelgarten – Business Card</title>
<link rel="stylesheet" href="https://fonts.googleapis.com/css2?family=Cinzel:wght@400&family=Source+Sans+3:wght@400&display=swap">
<style>
  :root {
    --bg: #e4e4e2;
    --taupe: #7e6a59;
    --taupe-dark: #6f5d4e;
    --cream: #f1ebe4;
    --disc: #e3d9cf;
    --paper: #ffffff;
    --ink: #7e6a59;
    --shadow: rgba(40, 30, 20, 0.22);
  }
  * { box-sizing: border-box; margin: 0; padding: 0; }
  html, body { width: 1200px; height: 963px; overflow: hidden; }
  body {
    background: var(--bg);
    display: flex;
    flex-direction: column;
    align-items: center;
    justify-content: center;
    gap: 70px;
  }
  .card {
    width: 560px;
    height: 320px;
    box-shadow: 0 10px 26px var(--shadow);
    position: relative;
    overflow: hidden;
  }

  /* Front */
  .card-front {
    background: var(--taupe);
    display: flex;
    flex-direction: column;
    align-items: center;
    justify-content: center;
  }
  .brand-disc {
    width: 92px;
    height: 92px;
    border-radius: 50%;
    background: var(--disc);
    margin-bottom: 16px;
  }
  .card-front .brand-disc { width: 104px; height: 104px; }
  .brand-name {
    font-family: "Cinzel", serif;
    font-size: 30px;
    letter-spacing: 2px;
    color: var(--cream);
    line-height: 1;
  }
  .brand-url {
    font-family: "Cinzel", serif;
    font-size: 9px;
    letter-spacing: 4px;
    color: var(--cream);
    margin-top: 6px;
  }

  /* Back */
  .card-back {
    background: var(--paper);
    display: flex;
  }
  .back-panel {
    width: 38%;
    background: var(--taupe);
    display: flex;
    flex-direction: column;
    align-items: center;
    justify-content: center;
  }
  .back-panel .brand-name { font-size: 22px; letter-spacing: 1.5px; }
  .back-panel .brand-url { font-size: 7px; letter-spacing: 3px; }
  .back-panel .brand-disc { width: 80px; height: 80px; margin-bottom: 12px; }

  .contact-side {
    flex: 1;
    padding: 62px 36px 0 20px;
    text-align: right;
    color: var(--ink);
  }
  .person-name {
    font-family: "Cinzel", serif;
    font-size: 22px;
    letter-spacing: 1px;
  }
  .person-title {
    font-family: "Cinzel", serif;
    font-size: 8px;
    letter-spacing: 2px;
    margin-top: 4px;
  }
  .contact-list {
    list-style: none;
    margin-top: 42px;
    font-family: "Source Sans 3", sans-serif;
    font-size: 17px;
    line-height: 25px;
  }
  .contact-list li {
    display: flex;
    justify-content: flex-end;
    align-items: center;
    gap: 12px;
  }
  .contact-list svg { width: 14px; height: 14px; fill: var(--ink); flex: none; }
</style>
</head>
<body>

  <section class="card card-front" aria-label="Card front">
    <div class="brand-disc"></div>
    <div class="brand-name">Zottelgarten</div>
    <div class="brand-url">WWW.ZOTTELGARTEN.CH</div>
  </section>

  <section class="card card-back" aria-label="Card back">
    <div class="back-panel">
      <div class="brand-disc"></div>
      <div class="brand-name">Zottelgarten</div>
      <div class="brand-url">WWW.ZOTTELGARTEN.CH</div>
    </div>
    <div class="contact-side">
      <div class="person-name">Persons Name</div>
      <div class="person-title">PERSONS TITLE</div>
      <ul class="contact-list">
        <li>999-777-5555
          <svg viewBox="0 0 16 16" aria-hidden="true"><path d="M3.6 1.2l2.3 2.6-1.2 1.8c.9 2 2.6 3.7 4.6 4.6l1.8-1.2 2.6 2.3-1.4 2.3C7.2 13.4 2.6 8.8 1.3 3.6z"/></svg>
        </li>
        <li>aaaaa@nnn.com
          <svg viewBox="0 0 16 16" aria-hidden="true"><path d="M1 3h14v1.2L8 9 1 4.2zM1 5.6l7 4.8 7-4.8V13H1z"/></svg>
        </li>
        <li>www.zottelgarten.ch
          <svg viewBox="0 0 16 16" aria-hidden="true"><path d="M8 1a7 7 0 100 14A7 7 0 008 1zm0 1.4c.8 0 1.7 1.5 2 3.6H6c.3-2.1 1.2-3.6 2-3.6zM2.5 7.2h2.4c0 .6 0 1.1.1 1.6H2.5a5.6 5.6 0 010-1.6zm3.8 0h3.4a14 14 0 010 1.6H6.3a14 14 0 010-1.6zm4.8 0h2.4a5.6 5.6 0 010 1.6h-2.4c.1-.5.1-1 0-1.6zM6 10h4c-.3 2.1-1.2 3.6-2 3.6S6.3 12.1 6 10z"/></svg>
        </li>
      </ul>
    </div>
  </section>

</body>
</html>
```